Safety Work Area Signage to keep people away from work zone

We would like to create a simple design that will include our logo and phone number, 'work area', and 'caution / cuidado' (please see a mock-up of the intended design in the uploaded files). Please provide multiple options. We would like a Professional look for the poster as it is meant for safety. Poster Size to be: 18.16" X 23.10"

Target Market(s)

General Public on Construction Sites

Font styles to use
Serif

Requirements
Must have
• see mock-ups in uploaded files
Nice to have
• Simple Design, Professional Look

```html
<!DOCTYPE html>
<html lang="en">
<head>
<meta charset="utf-8">
<title>Caution Work Area Signs</title>
<link rel="stylesheet" href="https://fonts.googleapis.com/css2?family=Arimo:wght@700&display=swap">
<style>
  :root {
    --backdrop: #5e5e5e;
    --safety-yellow: #fde428;
    --sign-black: #262626;
    --white: #ffffff;
  }
  * { margin: 0; padding: 0; box-sizing: border-box; }
  html, body {
    width: 1200px;
    height: 878px;
    overflow: hidden;
    background: var(--backdrop);
  }
  .canvas {
    position: relative;
    width: 1200px;
    height: 878px;
    font-family: "Arimo", Arial, sans-serif;
    font-weight: 700;
  }
  .sign {
    position: absolute;
    top: 113px;
    width: 512px;
    height: 652px;
    background: var(--safety-yellow);
    overflow: hidden;
    box-shadow: 0 3px 8px rgba(0, 0, 0, 0.35);
    color: var(--sign-black);
  }
  .sign--light-badge { left: 62px; }
  .sign--dark-badge { left: 616px; }

  .hazard-stripes {
    position: absolute;
    left: 0;
    width: 512px;
    height: 15px;
    display: block;
  }
  .hazard-stripes--top { top: 9px; }
  .hazard-stripes--under-header { top: 136px; }
  .hazard-stripes--bottom { top: 637px; }

  .caution-header {
    position: absolute;
    top: 31px;
    left: 0;
    width: 100%;
    height: 98px;
    background: var(--sign-black);
  }
  .caution-header__icon {
    position: absolute;
    left: 34px;
    top: 13px;
    width: 77px;
    height: 68px;
  }
  .caution-header__label {
    position: absolute;
    left: 130px;
    top: 18px;
    font-size: 67px;
    line-height: 1;
    letter-spacing: 3px;
    color: var(--white);
  }

  .headline {
    position: absolute;
    left: 0;
    width: 100%;
    text-align: center;
    font-size: 100px;
    line-height: 1;
  }
  .headline--work { top: 157px; left: -7px; }
  .headline--area { top: 245px; left: -7px; }

  .company-badge {
    position: absolute;
    left: 171px;
    top: 344px;
    width: 160px;
    height: 160px;
    border-radius: 50%;
    border: 14px solid var(--sign-black);
    display: flex;
    align-items: center;
    justify-content: center;
    text-align: center;
  }
  .sign--light-badge .company-badge {
    background: var(--white);
    box-shadow: 0 0 0 4px var(--white);
  }
  .sign--dark-badge .company-badge {
    background: transparent;
  }
  .company-badge__name {
    font-size: 21px;
    line-height: 1.1;
    color: var(--sign-black);
  }

  .contact-phone {
    position: absolute;
    left: -7px;
    top: 511px;
    width: 100%;
    text-align: center;
    font-size: 41px;
    line-height: 1;
  }
  .caution-spanish {
    position: absolute;
    left: 0;
    top: 550px;
    width: 100%;
    text-align: center;
    font-size: 83px;
    line-height: 1;
  }
</style>
</head>
<body>
<main class="canvas">
  <svg width="0" height="0" style="position:absolute">
    <defs>
      <pattern id="hazard-pattern" width="25.5" height="15" patternUnits="userSpaceOnUse" patternTransform="translate(12 0) skewX(-35)">
        <rect x="0" y="0" width="14" height="15" fill="#262626"/>
      </pattern>
    </defs>
  </svg>

  <section class="sign sign--light-badge" aria-label="Caution work area sign, light badge">
    <svg class="hazard-stripes hazard-stripes--top" viewBox="0 0 512 15"><rect width="512" height="15" fill="url(#hazard-pattern)"/></svg>
    <header class="caution-header">
      <svg class="caution-header__icon" viewBox="0 0 77 68" aria-hidden="true">
        <path d="M33 5 Q38.5 -2 44 5 L75 58 Q78 66 69 67 L8 67 Q-1 66 2 58 Z" fill="#ffffff"/>
        <rect x="34" y="21" width="9" height="25" fill="#262626"/>
        <rect x="34" y="51" width="9" height="8" fill="#262626"/>
      </svg>
      <span class="caution-header__label">CAUTION</span>
    </header>
    <svg class="hazard-stripes hazard-stripes--under-header" viewBox="0 0 512 15"><rect width="512" height="15" fill="url(#hazard-pattern)"/></svg>
    <h1 class="headline headline--work">WORK</h1>
    <h1 class="headline headline--area">AREA</h1>
    <div class="company-badge"><span class="company-badge__name">Harlan &amp; Sons<br>Builders</span></div>
    <p class="contact-phone">(555) 014-2290</p>
    <p class="caution-spanish">CUADADO</p>
    <svg class="hazard-stripes hazard-stripes--bottom" viewBox="0 0 512 15"><rect width="512" height="15" fill="url(#hazard-pattern)"/></svg>
  </section>

  <section class="sign sign--dark-badge" aria-label="Caution work area sign, outlined badge">
    <svg class="hazard-stripes hazard-stripes--top" viewBox="0 0 512 15"><rect width="512" height="15" fill="url(#hazard-pattern)"/></svg>
    <header class="caution-header">
      <svg class="caution-header__icon" viewBox="0 0 77 68" aria-hidden="true">
        <path d="M33 5 Q38.5 -2 44 5 L75 58 Q78 66 69 67 L8 67 Q-1 66 2 58 Z" fill="#ffffff"/>
        <rect x="34" y="21" width="9" height="25" fill="#262626"/>
        <rect x="34" y="51" width="9" height="8" fill="#262626"/>
      </svg>
      <span class="caution-header__label">CAUTION</span>
    </header>
    <svg class="hazard-stripes hazard-stripes--under-header" viewBox="0 0 512 15"><rect width="512" height="15" fill="url(#hazard-pattern)"/></svg>
    <h1 class="headline headline--work">WORK</h1>
    <h1 class="headline headline--area">AREA</h1>
    <div class="company-badge"><span class="company-badge__name">Harlan &amp; Sons<br>Builders</span></div>
    <p class="contact-phone">(555) 014-2290</p>
    <p class="caution-spanish">CUADADO</p>
    <svg class="hazard-stripes hazard-stripes--bottom" viewBox="0 0 512 15"><rect width="512" height="15" fill="url(#hazard-pattern)"/></svg>
  </section>
</main>
</body>
</html>
```